Need a Revamped Website - WaveCrestHub.com

I am looking for a website designed for www.wavecresthub.com
The present website has content relating to the Kafue Airwave Forum - an annual meeting for radio practitioners in Zambia. My intention is to change the focus: to make the website a resource hub for radio practitioners in Africa. The site is to have the following:
Featured articles (opinion pieces) contributed by industry insiders.
Links to various radio stations websites
An events calendar focusing on radio related events
News (radio industry updates) etc
The site should also be able to incorporate social media mechanisms such as 'Likes' through to Chatterbook or articles to be shared on Pipline etc.
The focus of the word Summit, for the purposes of the website, should shift. Instead of the meaning "meeting/ convention", it'll shift to connote "height, pinnacle (of radio excellence)".
The design should have a modern, contemporary feel.
Target Market(s)
The main target audience is radio deejays, radio station management, marketers/ advertisers, journalists.

```html
<!DOCTYPE html>
<html lang="en">
<head>
<meta charset="utf-8">
<title>WaveCrest Hub</title>
<link href="https://fonts.googleapis.com/css2?family=Open+Sans:wght@300;400;600;700&display=swap" rel="stylesheet">
<style>
:root{
  --orange:#e9a02c;
  --accent:#f0a52a;
  --brown:#3b2213;
  --brown-mid:#4a2c19;
  --brown-dark:#2c170c;
  --cream:#fdf3dc;
  --panel-grey:#efefef;
  --text:#222;
  --date:#e08a1e;
  --line:#d9d1c3;
  --white:#fff;
}
*{box-sizing:border-box;margin:0;padding:0}
html,body{width:975px;height:1200px;overflow:hidden}
body{font-family:"Open Sans",Arial,sans-serif;color:var(--text);background:linear-gradient(#fbe9c2 0,var(--cream) 220px,#fdf6e6 600px,#fdf4e0 100%);position:relative;font-size:10px}
a{color:inherit;text-decoration:none}

.top-nav{position:absolute;top:0;left:0;width:975px;height:47px;background:linear-gradient(#f4b447,var(--orange));border-top:6px solid #e8e3d8;display:flex;justify-content:center;align-items:center}
.top-nav a{font-weight:700;font-size:13.5px;color:var(--brown-dark);padding:0 22px}
.top-nav a.active{color:#8a3e10}
.star{font-size:12px;color:var(--brown-dark)}

.header{position:absolute;top:47px;left:0;width:975px;height:100px;background:linear-gradient(var(--brown-mid),var(--brown))}
.logo{position:absolute;left:34px;top:28px;font-weight:700;font-size:37px;color:var(--white);letter-spacing:-0.5px}
.tagline{position:absolute;left:368px;top:42px;color:#f2e6d6;font-size:11.5px;line-height:13.5px}
.search{position:absolute;left:758px;top:40px;width:176px;height:26px;border-radius:13px;background:linear-gradient(#fff,#e8e8e8);border:1px solid #cfc6bc}
.search svg{position:absolute;right:10px;top:5px}
.search::before{content:"";position:absolute;right:29px;top:3px;height:18px;border-left:1px solid #ccc}

.slider{position:absolute;left:27px;top:168px;width:918px;height:296px;background:var(--white);border:1px solid #e4dccd;border-radius:3px;box-shadow:0 1px 3px rgba(0,0,0,.08)}
.slide-photo{position:absolute;left:7px;top:7px;width:903px;height:280px;background:linear-gradient(180deg,#b9a580 0%,#c8b38c 25%,#d9d4cc 55%,#c8c2ba 80%,#aaa 100%)}
.slide-caption{position:absolute;left:7px;bottom:8px;width:903px;height:44px;background:rgba(240,238,235,.88);font-weight:300;font-size:24px;color:#3a2a22;padding:8px 15px;letter-spacing:-0.3px}
.slide-caption b{font-weight:400}
.arrow{position:absolute;top:112px;width:35px;height:35px;border-radius:50%;background:var(--white);border:1px solid #ccc;box-shadow:0 1px 3px rgba(0,0,0,.2)}
.arrow svg{position:absolute;left:12px;top:11px}
.arrow.prev{left:-9px}.arrow.next{right:-9px}

.breadcrumb{position:absolute;left:40px;top:477px;font-size:10px;color:#333;display:flex;gap:7px;align-items:center}

.box{position:absolute;background:var(--white);border:1px solid #ddd;box-shadow:0 1px 2px rgba(0,0,0,.06);overflow:hidden}
.box-head{height:37px;background:linear-gradient(var(--brown-mid),var(--brown-dark));color:var(--white);font-size:14px;padding:10px 14px;position:relative}
.box-head b{color:var(--accent);font-weight:700}
.tag{position:absolute;right:10px;top:10px;background:#a85a12;color:#fff;font-size:10px;padding:2px 6px;border:1px solid #c07a2a}

.about{left:27px;top:500px;width:635px;height:158px}
.about p{font-size:10px;line-height:13.8px;color:#222;padding:0 13px;letter-spacing:-0.1px}
.about p.first{padding-top:10px}
.about p.body{width:460px}
.more{color:var(--date);margin-left:6px}
.dishes{position:absolute;right:10px;bottom:8px;width:175px;height:45px;background:radial-gradient(ellipse at 70% 60%,#d8d8d8,rgba(255,255,255,0) 70%)}

.featured{left:27px;top:670px;width:635px;height:428px}
.article{padding:14px 13px 0;height:68px}
.article h3{font-size:10.5px;font-weight:700;margin-bottom:1px}
.article p{font-size:10px;line-height:13.8px;letter-spacing:-0.1px}
.meta{height:44px;background:var(--panel-grey);display:flex;align-items:center;padding:0 13px;font-size:10px;color:#222;gap:11px;margin:7px 1px 0}
.meta u{color:#222}
.sep{color:#555}
.like{border:1px solid #b8c2d6;background:#f5f6fa;color:#3b5a99;padding:3px 5px;border-radius:2px}
.sq{display:inline-block;width:12px;height:12px;background:#3b5a99;vertical-align:middle;margin-right:4px}
.sq.pip{background:#2fa9e0;margin-left:4px}

.news{left:673px;top:500px;width:272px;height:405px}
.news-item{padding:11px 13px 0;border-bottom:1px solid var(--line);overflow:hidden}
.news-item.n1{height:127px}
.news-item.n2{height:125px}
.news-item.n3{border-bottom:none;height:114px}
.news-item h4{font-size:10px;font-weight:700;line-height:13px;letter-spacing:-0.1px}
.news-item .date{color:var(--date);font-size:9px;line-height:12px;margin:1px 0 12px}
.news-item p{font-size:9.5px;line-height:13.5px;letter-spacing:-0.15px}
.news-item .more{margin-left:4px}

.events{left:673px;top:918px;width:272px;height:180px}
.ev-title{position:absolute;left:12px;top:10px;font-size:13.5px;line-height:13.5px;color:#2c170c}
.ev-title b{font-weight:700}
.ev-icon{position:absolute;left:14px;top:46px;width:55px;height:55px;background:linear-gradient(#e6a98a,#f6e0d4);border:1px solid #d4b9a6}
.ev-brand{position:absolute;left:14px;top:108px;font-size:12px;font-weight:700;color:#c9c9c9;line-height:13px;width:70px}
.ev-nav{position:absolute;left:16px;top:154px;display:flex;gap:2px}
.ev-nav span{width:16px;height:16px;border:1px solid #bbb;background:#f8f8f8;display:flex;align-items:center;justify-content:center}
.calendar{position:absolute;left:97px;top:10px;width:171px;border-collapse:separate;border-spacing:2px;background:#e2ded6;font-size:10px;text-align:center}
.calendar caption{background:linear-gradient(#f2ece0,#d8d0c2);font-weight:700;font-size:12.5px;padding:3px 0;color:#2c170c}
.calendar th{background:#d6d0c6;font-size:9px;height:11px}
.calendar td{background:#cfcac3;height:17px;color:#222}
.calendar td.out{background:#ebe8e3;color:#aaa}
.calendar td.hl{background:#6b4d3b;color:#fff}
.calendar td.hl2{background:#8b7b70;color:#fff}

.footer{position:absolute;left:0;top:1112px;width:975px;height:88px;border-top:4px solid var(--orange);background:var(--brown)}
.footer-nav{height:44px;display:flex;justify-content:center;align-items:center;background:linear-gradient(var(--brown-mid),var(--brown))}
.footer-nav a{color:#fff;font-weight:700;font-size:13.5px;padding:0 23px}
.footer-nav .star{color:#fff}
.copyright{height:40px;background:var(--brown-dark);color:#eee;text-align:center;font-size:10.5px;padding-top:13px}
</style>
</head>
<body>

<nav class="top-nav">
  <a class="active" href="#">HOME</a><span class="star">★</span>
  <a href="#">ABOUT</a><span class="star">★</span>
  <a href="#">ARTICLES</a><span class="star">★</span>
  <a href="#">GALLERY</a><span class="star">★</span>
  <a href="#">PARTNERS</a><span class="star">★</span>
  <a href="#">EVENTS</a><span class="star">★</span>
  <a href="#">CONTACT</a>
</nav>

<header class="header">
  <div class="logo">WAVECREST HUB</div>
  <div class="tagline">BETTER PROGRAMMING. FREE SPEECH.<br>INTELLIGENT COMMUNICATION. GREAT ENTERTAINMENT</div>
  <div class="search">
    <svg width="14" height="14" viewBox="0 0 14 14"><circle cx="5.5" cy="5.5" r="4" fill="none" stroke="#333" stroke-width="1.6"/><line x1="8.5" y1="8.5" x2="12.5" y2="12.5" stroke="#333" stroke-width="2"/></svg>
  </div>
</header>

<section class="slider">
  <div class="slide-photo" role="img" aria-label="Group photo of smiling radio practitioners wearing lanyards in front of a building"></div>
  <div class="slide-caption"><b>WAVECREST HUB</b> - A RESOURCE HUB FOR <b>RADIO PRACTITIONERS</b> IN AFRICA</div>
  <span class="arrow prev"><svg width="9" height="12" viewBox="0 0 9 12"><path d="M7 1 2 6l5 5" fill="none" stroke="#222" stroke-width="2.4"/></svg></span>
  <span class="arrow next"><svg width="9" height="12" viewBox="0 0 9 12"><path d="M2 1l5 5-5 5" fill="none" stroke="#222" stroke-width="2.4"/></svg></span>
</section>

<div class="breadcrumb">
  <svg width="10" height="9" viewBox="0 0 10 9"><path d="M5 0 0 4.5h1.5V9h2.5V6h2v3h2.5V4.5H10Z" fill="#7a4a28"/></svg>
  <span>WaveCrest Hub</span>
</div>

<section class="box about">
  <div class="box-head">ABOUT <b>WAVECREST HUB</b></div>
  <p class="first">Lorem ipsum dolor sit amet consectetur adipiscing elit. Sed accumsan tempus lobortis. Pellentesque habitant morbi tristique senectus et netus et malesuada fames ac turpis egestas.</p>
  <p class="body">Fusce diam libero congue vel volutpat ut faucibus non arcu. Donec mollis sem nec mollis vehicula turpis turpis convallis velit nec volutpat tellus ante sit amet erat. Nunc ipsum lectus commodo in rutrum in suscipit ut lorem. Quisque vitae ipsum pharetra purus eleifend consectetur et id lorem. Praesent mollis magna id risus tristique sed facilisis quam egestas.<span class="more">read more...</span></p>
  <div class="dishes" role="img" aria-label="Faint row of satellite dishes"></div>
</section>

<section class="box featured">
  <div class="box-head">FEATURED <b>ARTICLES</b><span class="tag">Read all</span></div>

  <article class="article">
    <h3>Lorem ipsum dolor sit amet consectetur adipiscing elit.</h3>
    <p>Sed accumsan tempus lobortis. Pellentesque habitant morbi tristique senectus et netus et malesuada fames ac turpis egestas. Fusce diam libero congue volutpat. Praesent mollis magna id risus tristique sed facilisis quam egestas. Nulla congue, elit eget mattis fermentum, sem enim auctor lacus, quis viverra augue mauris sit amet enim.<span class="more">read more...</span></p>
  </article>
  <div class="meta"><span>Posted by: <u>Tomas Mwale</u></span><span class="sep">|</span><span>March 03, 2011</span><span class="sep">|</span><span class="like">Like</span><span><span class="sq"></span>3 people like this.</span><span class="sep">|</span><span>Share this on<span class="sq pip"></span></span></div>

  <article class="article">
    <h3>Lorem ipsum dolor sit amet consectetur adipiscing elit.</h3>
    <p>Sed accumsan tempus lobortis. Pellentesque habitant morbi tristique senectus et netus et malesuada fames ac turpis egestas. Fusce diam libero congue volutpat. Praesent mollis magna id risus tristique sed facilisis quam egestas. Nulla congue, elit eget mattis fermentum, sem enim auctor lacus, quis viverra augue mauris sit amet enim.<span class="more">read more...</span></p>
  </article>
  <div class="meta"><span>Posted by: <u>Tomas Mwale</u></span><span class="sep">|</span><span>March 03, 2011</span><span class="sep">|</span><span class="like">Like</span><span><span class="sq"></span>3 people like this.</span><span class="sep">|</span><span>Share this on<span class="sq pip"></span></span></div>

  <article class="article">
    <h3>Lorem ipsum dolor sit amet consectetur adipiscing elit.</h3>
    <p>Sed accumsan tempus lobortis. Pellentesque habitant morbi tristique senectus et netus et malesuada fames ac turpis egestas. Fusce diam libero congue volutpat. Praesent mollis magna id risus tristique sed facilisis quam egestas. Nulla congue, elit eget mattis fermentum, sem enim auctor lacus, quis viverra augue mauris sit amet enim.<span class="more">read more...</span></p>
  </article>
  <div class="meta"><span>Posted by: <u>Tomas Mwale</u></span><span class="sep">|</span><span>March 03, 2011</span><span class="sep">|</span><span class="like">Like</span><span><span class="sq"></span>3 people like this.</span><span class="sep">|</span><span>Share this on<span class="sq pip"></span></span></div>
</section>

<section class="box news">
  <div class="box-head">RADIO <b>NEWS</b><span class="tag">RSS</span></div>
  <div class="news-item n1">
    <h4>Lorem ipsum dolor sit amet consectetur adipiscing elit.</h4>
    <div class="date">March 24, 2011</div>
    <p>Pellentesque habitant morbi tristique senectus et netus et malesuada fames ac turpis egestas. Fusce diam libero congue vel volutpat ut faucibus non arcu.<span class="more">read more...</span></p>
  </div>
  <div class="news-item n2">
    <h4>Donec mollis sem nec mollis vehicula turpis turpis convallis velit nec.</h4>
    <div class="date">March 24, 2011</div>
    <p>Nunc ipsum lectus commodo in rutrum in suscipit ut lorem. Quisque vitae ipsum pharetra purus eleifend consectetur et id lorem. Praesent mollis magna id risus tristique sed facilisis quam.<span class="more">read more...</span></p>
  </div>
  <div class="news-item n3">
    <h4>Nulla congue elit eget mattis fermentum, sem enim auctor lacus quis viverra.</h4>
    <div class="date">March 24, 2011</div>
    <p>Proin laoreet rhoncus orci, nec sagittis odio ornare eget. Aenean ligula arcu, dapibus non fermentum ut iaculis sit amet massa.<span class="more">read more...</span></p>
  </div>
</section>

<section class="box events">
  <div class="ev-title">LATEST<br><b>EVENTS</b></div>
  <div class="ev-icon" role="img" aria-label="Calendar page illustration"></div>
  <div class="ev-brand">WAVECREST HUB</div>
  <div class="ev-nav">
    <span><svg width="5" height="7" viewBox="0 0 5 7"><path d="M4 0 0 3.5 4 7Z" fill="#555"/></svg></span>
    <span><svg width="5" height="7" viewBox="0 0 5 7"><path d="M1 0l4 3.5L1 7Z" fill="#555"/></svg></span>
  </div>
  <table class="calendar">
    <caption>April 2011</caption>
    <tr><th>S</th><th>M</th><th>T</th><th>W</th><th>T</th><th>F</th><th>S</th></tr>
    <tr><td class="out">27</td><td class="out">28</td><td class="out">29</td><td class="out">30</td><td class="out">31</td><td>1</td><td>2</td></tr>
    <tr><td>3</td><td>4</td><td>5</td><td>6</td><td>7</td><td>8</td><td>9</td></tr>
    <tr><td>10</td><td class="hl">11</td><td class="hl2">12</td><td class="hl">13</td><td class="hl2">14</td><td class="hl">15</td><td class="hl2">16</td></tr>
    <tr><td class="hl">17</td><td>18</td><td>19</td><td>20</td><td>21</td><td>22</td><td>23</td></tr>
    <tr><td>24</td><td>25</td><td>26</td><td>27</td><td>28</td><td>29</td><td>30</td></tr>
    <tr><td class="out">1</td><td class="out">2</td><td class="out">3</td><td class="out">4</td><td class="out">5</td><td class="out">6</td><td class="out">7</td></tr>
  </table>
</section>

<footer class="footer">
  <nav class="footer-nav">
    <a href="#">HOME</a><span class="star">★</span>
    <a href="#">ABOUT</a><span class="star">★</span>
    <a href="#">ARTICLES</a><span class="star">★</span>
    <a href="#">GALLERY</a><span class="star">★</span>
    <a href="#">PARTNERS</a><span class="star">★</span>
    <a href="#">EVENTS</a><span class="star">★</span>
    <a href="#">CONTACT</a>
  </nav>
  <div class="copyright">© WaveCrest Hub 2011. All Rights Reserved. Terms of Use. Privacy Policy.</div>
</footer>

</body>
</html>
```